Business Card design for a mini spa

business card for a small natural skincare/waxing spa. I need a modern, clean, classy card that draws people in but also need to be able to write future appointments on one side of it.

Target Market(s)

women age 16-70

Industry/Entity Type

Beauty Salon

Contact Information for Business Card

Fernlight Skin Care 907-318-2796
2958 W Talvenby Kodiak, AK 99615
Facial, Waxing, Spray Tanning,

Colors
33b8a4

Requirements
Must have
• Fernlight logo with flower
• my tag line "quiet roots bright bloom"
• 907-318-2796
• 2958 W Talvenby
• a place to write ......Your Next Appointment
• Mira Oskenfeld
Nice to have
• something modern, elegant, clean and simple with my attached logo. I also attached a few pictures of what I like along with a color pallet and a few fonts that I like.
Should not have
• no pictures of people in a spa I do not want your typical spa pictures like stone, people receiving a treatment.

```html
<!DOCTYPE html>
<html lang="en">
<head>
<meta charset="utf-8">
<title>Fernlight Skin Care – Business Card</title>
<link href="https://fonts.googleapis.com/css2?family=Amatic+SC:wght@400;700&family=Quicksand:wght@400;500&display=swap" rel="stylesheet">
<style>
  :root {
    --backdrop: #2d2d2e;
    --paper: #ffffff;
    --teal: #33b8a4;
    --teal-soft: #a2dcd8;
    --teal-deep: #7cc4c0;
    --peach: #e2a27a;
    --front-tan: #c6a77d;
    --front-sage: #a9b98f;
    --front-green: #6fae92;
    --ink-light: #f5f7f0;
  }
  * { box-sizing: border-box; margin: 0; padding: 0; }
  html, body {
    width: 1200px; height: 900px; overflow: hidden;
    background: var(--backdrop);
  }
  .stage {
    position: relative; width: 1200px; height: 900px;
    display: flex; align-items: center; justify-content: center; gap: 80px;
  }
  .card {
    position: relative; width: 340px; height: 595px; overflow: hidden;
    box-shadow: 0 18px 40px rgba(0,0,0,.45);
  }

  /* Front */
  .card-front { color: var(--ink-light); }
  .front-backdrop {
    position: absolute; inset: 0;
    background:
      radial-gradient(circle at 0% 0%, rgba(226,162,122,.75), rgba(226,162,122,0) 45%),
      linear-gradient(170deg, var(--front-tan) 0%, var(--front-sage) 40%, var(--front-green) 100%);
  }
  .front-brand {
    position: absolute; left: 0; right: 0; top: 395px; text-align: center;
  }
  .brand-name {
    font-family: "Amatic SC", sans-serif; font-weight: 400;
    font-size: 64px; line-height: 1; letter-spacing: 2px;
  }
  .brand-mark {
    display: inline-block; width: 12px; height: 12px; border-radius: 50%;
    border: 1.5px solid currentColor; margin-left: 6px; vertical-align: 10px;
  }
  .brand-sub {
    font-family: "Quicksand", sans-serif; font-size: 13px; letter-spacing: 3px;
    text-transform: uppercase; margin-top: 2px;
  }
  .front-tagline {
    font-family: "Amatic SC", sans-serif; font-weight: 700;
    font-size: 26px; letter-spacing: 1px; text-transform: uppercase; margin-top: 8px;
  }

  /* Back */
  .card-back { background: var(--paper); }
  .back-header { height: 215px; padding-top: 42px; text-align: center; }
  .back-header .brand-name { color: var(--teal); font-size: 46px; }
  .back-header .brand-sub { color: var(--peach); font-size: 11px; }
  .back-tagline {
    font-family: "Amatic SC", sans-serif; font-weight: 700; color: var(--teal);
    font-size: 17px; text-transform: uppercase; letter-spacing: 1px; margin-top: 10px;
  }
  .contact-list {
    list-style: none; margin-top: 12px; display: inline-block; text-align: left;
    font-family: "Amatic SC", sans-serif; font-weight: 700; color: var(--teal);
    font-size: 20px; letter-spacing: 1px;
  }
  .contact-list li { display: flex; align-items: center; gap: 12px; line-height: 1.35; }
  .contact-list svg { width: 14px; height: 14px; }

  .back-band {
    position: absolute; left: 0; right: 0; top: 215px; bottom: 0;
    background: var(--teal-soft);
  }
  .band-decoration {
    position: absolute; left: 0; right: 0; top: 0; bottom: 0;
    background: radial-gradient(ellipse at 60% 30%, var(--teal-deep) 0%, rgba(124,196,192,0) 60%);
    opacity: .55;
  }
  .appointment-field {
    position: absolute; left: 0; right: 0; top: 128px; height: 80px;
    background: var(--paper);
  }
  .appointment-rule {
    position: absolute; left: 22px; right: 22px; top: 220px;
    border-top: 3px dotted var(--paper);
  }
  .appointment-label {
    position: absolute; left: 0; right: 0; top: 238px; text-align: center;
    font-family: "Amatic SC", sans-serif; font-weight: 700; color: var(--paper);
    font-size: 30px; letter-spacing: 1px;
  }
</style>
</head>
<body>
<main class="stage">
  <section class="card card-front" aria-label="Card front">
    <div class="front-backdrop" role="img" aria-label="Soft sage and peach gradient with scattered light sparkles"></div>
    <div class="front-brand">
      <div class="brand-name">Fernlight<span class="brand-mark"></span></div>
      <div class="brand-sub">Skin Care</div>
      <div class="front-tagline">quiet roots bright bloom</div>
    </div>
  </section>

  <section class="card card-back" aria-label="Card back">
    <header class="back-header">
      <div class="brand-name">Fernlight</div>
      <div class="brand-sub">Skin Care</div>
      <div class="back-tagline">quiet roots bright bloom</div>
      <ul class="contact-list">
        <li>
          <svg viewBox="0 0 24 24" aria-hidden="true"><path fill="#33b8a4" d="M6.6 10.8a15 15 0 0 0 6.6 6.6l2.2-2.2a1 1 0 0 1 1-.25 11.4 11.4 0 0 0 3.6.57 1 1 0 0 1 1 1V20a1 1 0 0 1-1 1A17 17 0 0 1 3 4a1 1 0 0 1 1-1h3.5a1 1 0 0 1 1 1c0 1.25.2 2.45.57 3.6a1 1 0 0 1-.25 1z"/></svg>
          907-318-2796
        </li>
        <li>
          <svg viewBox="0 0 24 24" aria-hidden="true"><path fill="#33b8a4" d="M21 3 3 10.5l7.5 3 3 7.5z"/></svg>
          2958 W Talvenby
        </li>
      </ul>
    </header>
    <div class="back-band">
      <div class="band-decoration" role="img" aria-label="Large faint outline flower motif in deeper teal"></div>
      <div class="appointment-field"></div>
      <div class="appointment-rule"></div>
      <div class="appointment-label">Your Next Appointment</div>
    </div>
  </section>
</main>
</body>
</html>
```